Road Sign at our office 84 in X 48 in - Small Billboard

Kestrel Electrical
Electrical & Lighting Services

- we need a sign design for our small business/company based in Calhoun, GA called Kestrel Electrical - "our mission is to provide Northwest Georgia with dependable, high-quality electrical services that prioritize safety, integrity, and long-term reliability. As a woman-owned business with over 25 years of experience, we are committed to delivering exceptional workmanship and personalized service for every commercial, residential, and industrial project we undertake. We stand behind our work with a lifetime warranty—because your trust is our most powerful connection."

display logo, phone number, and open to other ideas without being cluttered, maybe instead of full website address, just use @ksrelectrical and it will send them to all of our website and socials...

it needs to be easy to read as they drive down the road
this is a place where people may be traveling at high speeds, make sure it's easy to see and understand at a glance.
It will be hanging 20-24ft from the ground. Like a small billboard.

https://ksrelectricworks.com/

Industry/Entity Type

Electrical Contractor

Requirements
Nice to have
• match the look and feel of website and socials

```html
<!DOCTYPE html>
<html lang="en">
<head>
<meta charset="UTF-8">
<title>Kestrel Electrical – Road Sign</title>
<link href="https://fonts.googleapis.com/css2?family=Barlow:wght@600;700&display=swap" rel="stylesheet">
<style>
  :root {
    --ink: #111111;
    --sun: #f6b318;
    --ember: #f05a28;
    --blush: #f8e2d4;
    --blush-soft: #fcf1ea;
    --paper: #ffffff;
  }
  * { margin: 0; padding: 0; box-sizing: border-box; }
  html, body { width: 1200px; height: 687px; overflow: hidden; background: var(--paper); }
  .sign {
    position: relative;
    width: 1200px;
    height: 687px;
    background: var(--paper);
    font-family: "Barlow", Arial, sans-serif;
    color: var(--ink);
    overflow: hidden;
  }
  .backdrop-art {
    position: absolute;
    left: 700px;
    top: 0;
    width: 500px;
    height: 687px;
    background: radial-gradient(ellipse at 60% 45%, var(--blush) 0%, var(--blush-soft) 45%, rgba(255,255,255,0) 75%);
    opacity: 0.8;
  }
  .brand {
    position: absolute;
    left: 38px;
    top: 62px;
    display: flex;
    align-items: center;
    gap: 18px;
  }
  .brand-dot {
    width: 72px;
    height: 72px;
    border-radius: 50%;
    background: var(--ember);
  }
  .brand-name {
    font-weight: 700;
    color: var(--ink);
    line-height: 0.95;
  }
  .brand-name .line1 { display: block; font-size: 58px; }
  .brand-name .line2 { display: block; font-size: 24px; letter-spacing: 9px; margin-top: 4px; }
  .headline {
    position: absolute;
    left: 0;
    width: 1200px;
    top: 258px;
    text-align: center;
    font-size: 98px;
    font-weight: 700;
    line-height: 1;
    letter-spacing: 1px;
  }
  .tagline {
    position: absolute;
    left: 0;
    width: 1200px;
    top: 354px;
    text-align: center;
    font-size: 38px;
    font-weight: 700;
    letter-spacing: 3px;
    line-height: 1;
  }
  .call-label {
    position: absolute;
    left: 66px;
    top: 478px;
    font-size: 52px;
    font-weight: 700;
    line-height: 1;
  }
  .base-band {
    position: absolute;
    left: 0;
    top: 611px;
    width: 1200px;
    height: 60px;
    background: var(--ember);
  }
  .pill {
    position: absolute;
    top: 545px;
    height: 104px;
    background: var(--sun);
    display: flex;
    align-items: center;
    font-weight: 700;
    font-size: 74px;
    line-height: 1;
  }
  .pill-phone {
    left: 0;
    width: 548px;
    border-radius: 0 52px 52px 0;
    padding-left: 64px;
    box-shadow: 8px 8px 10px rgba(0,0,0,0.25);
  }
  .pill-handle {
    left: 651px;
    width: 549px;
    border-radius: 52px 0 0 52px;
    padding-left: 44px;
  }
</style>
</head>
<body>
  <main class="sign">
    <div class="backdrop-art" role="img" aria-label="Large faint brand emblem in soft peach tones"></div>

    <div class="brand">
      <span class="brand-dot"></span>
      <span class="brand-name">
        <span class="line1">Kestrel</span>
        <span class="line2">ELECTRICAL</span>
      </span>
    </div>

    <h1 class="headline">KESTREL ELECTRICAL</h1>
    <p class="tagline">ELECTRICAL &amp; LIGHTING SERVICES</p>

    <p class="call-label">Call Now</p>

    <div class="base-band"></div>
    <div class="pill pill-phone">706-555-0148</div>
    <div class="pill pill-handle">@ksrelectrical</div>
  </main>
</body>
</html>
```